Creative Website for Start Up in Italy

We need a wordpress design for a new start up based in Italy called "DoRuVi". Our start up takes a human-centered, design-based approach to help organizations in the public and private sectors innovate and grow. Through Participatory design we try to actively involve all stakeholders (e.g. employees, partners, customers, citizens, end users) in the design process to help ensure the final result meets their needs and is usable. The final design should recall our logo (see attachment) and should have the following setting: Home - Mission - About Us - What we Do - Portfolio - Blog - Contact Us. Moreover we would like a Responsive Multi-language, cross browser compatible, mobile ready website with a back office. Note that the designer should also do the implementation, meaning that we need a full website (including CSS and XHTML) as we already have a web hosting www.doruvi.it and a blog doruviblog.example-host.com

```html
<!DOCTYPE html>
<html lang="en">
<head>
<meta charset="utf-8">
<title>DoRuVi</title>
<link href="https://fonts.googleapis.com/css2?family=Open+Sans:wght@400;600;700&family=PT+Serif:wght@400;700&display=swap" rel="stylesheet">
<style>
:root{
  --blue:#0d55a4;
  --heading-blue:#1a5aa6;
  --grey-band:#e4e4e6;
  --text:#555a60;
  --dark:#2b2e33;
  --white:#ffffff;
  --green:#7cb342;
  --footer-text:#b9d3f0;
  --footer-line:#3a77bd;
  --icon-light:#8fb6e2;
}
*{box-sizing:border-box;margin:0;padding:0}
html,body{width:1200px;height:2479px;overflow:hidden;background:var(--white)}
body{position:relative;font-family:"Open Sans",Arial,sans-serif;color:var(--text)}
.abs{position:absolute}
.serif{font-family:"PT Serif",Georgia,serif}

/* header */
.site-header{position:absolute;left:0;top:0;width:1200px;height:157px;background:var(--white)}
.nav-link{position:absolute;top:50px;font-size:13px;color:#3a3d42;transform:translateX(-50%);white-space:nowrap}
.brand{position:absolute;left:600px;top:36px;transform:translateX(-50%);display:flex;align-items:center;gap:10px}
.brand-dot{width:22px;height:22px;border-radius:50%;background:var(--green)}
.brand-name{font-size:34px;font-weight:400;color:#5d6168}
.header-social{position:absolute;left:0;top:99px;width:1200px;display:flex;justify-content:center;gap:5px}
.header-social span{width:26px;height:26px;border:1.5px solid var(--heading-blue);border-radius:50%}

/* hero */
.hero{position:absolute;left:0;top:157px;width:1200px;height:545px;background:linear-gradient(135deg,#b9c4cf 0%,#e7ecf1 40%,#8e99a6 75%,#4b5560 100%)}
.hero-caption{position:absolute;left:0;top:425px;width:1200px;height:120px;background:rgba(20,22,26,.82)}
.hero-title{position:absolute;left:284px;top:20px;font-size:21px;color:var(--white);letter-spacing:.5px}
.hero-text{position:absolute;left:280px;top:52px;font-size:12.5px;line-height:23px;color:#e6e6e6}
.hero-arrow{position:absolute;top:471px;width:36px;height:36px;border-radius:50%;background:rgba(70,72,76,.9)}

/* what we do */
.what-we-do{position:absolute;left:0;top:702px;width:1200px;height:315px;background:var(--grey-band)}
.section-title{position:absolute;left:0;width:1200px;text-align:center;font-family:"PT Serif",Georgia,serif;font-size:23px;font-weight:400;color:var(--heading-blue);letter-spacing:.5px}
.service{position:absolute;top:78px;width:200px;text-align:center;transform:translateX(-50%)}
.service-icon{width:86px;height:86px;margin:0 auto;border-radius:50%;background:var(--blue);display:flex;align-items:center;justify-content:center;box-shadow:0 0 0 4px #d3d6dc}
.service-name{margin-top:16px;font-family:"PT Serif",Georgia,serif;font-size:17px;color:var(--dark);letter-spacing:.5px}
.service-text{margin-top:12px;font-size:12.5px;line-height:22.5px;color:var(--text)}

/* mission */
.mission-visual{position:absolute;left:132px;top:1071px;width:377px;height:326px;background:linear-gradient(180deg,#1b1c1f 0%,#2c2d31 70%,#c9cbcf 72%,#e2e3e6 100%);border-radius:8px}
.mission-title{position:absolute;left:587px;top:1086px;font-family:"PT Serif",Georgia,serif;font-size:21px;font-weight:400;color:var(--heading-blue)}
.mission-lead{position:absolute;left:587px;top:1128px;font-size:15.5px;font-weight:600;color:#333}
.mission-text{position:absolute;left:587px;width:480px;font-size:12.5px;line-height:23px;color:var(--text)}
.btn-primary{position:absolute;left:590px;top:1324px;width:167px;height:43px;background:var(--blue);color:var(--white);font-size:14px;font-weight:600;display:flex;align-items:center;justify-content:center;border-radius:2px}

/* portfolio */
.portfolio{position:absolute;left:0;top:1438px;width:1200px;height:385px;background:var(--grey-band)}
.portfolio-sub{position:absolute;left:0;top:77px;width:1200px;text-align:center;font-size:12.5px;color:var(--text)}
.work{position:absolute;top:122px;width:224px}
.work-img{width:224px;height:205px}
.work-link{margin-top:10px;text-align:center;font-size:12.5px;color:#333}

/* blog */
.blog-img{position:absolute;top:1912px;height:176px}
.blog-body{position:absolute;top:1903px;width:240px}
.blog-title{font-size:15.5px;line-height:24px;color:#333}
.blog-text{margin-top:12px;font-size:12.5px;line-height:24px;color:var(--text)}
.blog-meta{margin-top:12px;display:flex;align-items:center;gap:6px;font-size:12.5px;color:#333}

/* footer */
.site-footer{position:absolute;left:0;top:2121px;width:1200px;height:358px;background:var(--blue)}
.footer-col{position:absolute;top:32px;width:218px}
.footer-heading{font-family:"PT Serif",Georgia,serif;font-size:17px;color:var(--white);letter-spacing:.5px;padding-bottom:12px;border-bottom:1px solid var(--footer-line);width:218px}
.footer-text{font-size:12px;line-height:22.5px;color:var(--footer-text)}
.footer-brand{display:flex;align-items:center;gap:8px;margin-top:16px}
.footer-brand-dot{width:18px;height:18px;border-radius:50%;background:var(--white)}
.footer-brand-name{font-size:28px;color:var(--white)}
.tweet{display:flex;gap:10px;margin-top:14px}
.tweet-dot{flex:none;width:14px;height:14px;border-radius:50%;background:var(--icon-light);margin-top:4px}
.tweet-date{font-style:italic;color:#d7e5f6}
.contact-row{display:flex;align-items:center;gap:10px;height:45px;font-size:12px;color:var(--footer-text)}
.contact-row b{font-weight:400;color:var(--white)}
.field{width:207px;height:26px;background:var(--white);border:1px solid #cfd6de;margin-top:8px;font-size:12px;color:#333;padding:4px 10px}
.btn-login{width:99px;height:28px;background:var(--green);color:var(--white);font-size:13px;font-weight:600;display:flex;align-items:center;justify-content:center;margin-top:12px}
.footer-rule{position:absolute;left:132px;top:268px;width:936px;height:1px;background:var(--footer-line)}
.footer-copy{position:absolute;left:132px;top:292px;font-size:12px;color:#d7e5f6}
.footer-social{position:absolute;left:905px;top:287px;display:flex;gap:7px}
.footer-social span{width:26px;height:26px;border-radius:50%;background:var(--white)}
.footer-code{position:absolute;left:1130px;top:293px;font-size:12px;color:#c5d8ef}
</style>
</head>
<body>

<header class="site-header">
  <span class="nav-link" style="left:192px">Home</span>
  <span class="nav-link" style="left:269px">Mission</span>
  <span class="nav-link" style="left:356px">About Us</span>
  <span class="nav-link" style="left:456px">What we Do</span>
  <div class="brand"><span class="brand-dot"></span><span class="brand-name">DoRuVi</span></div>
  <span class="nav-link" style="left:815px">Portfolio</span>
  <span class="nav-link" style="left:891px">Blog</span>
  <span class="nav-link" style="left:974px">Contact Us</span>
  <svg class="abs" style="left:1028px;top:52px" width="16" height="16" viewBox="0 0 16 16"><circle cx="6.5" cy="6.5" r="4.5" fill="none" stroke="#2b2e33" stroke-width="2"/><line x1="10" y1="10" x2="14" y2="14" stroke="#2b2e33" stroke-width="2.2"/></svg>
  <div class="header-social"><span></span><span></span><span></span><span></span><span></span></div>
</header>

<section class="hero" role="img" aria-label="Photo of two smiling business colleagues working together at a desk">
  <div class="hero-caption">
    <div class="hero-title serif">INCLUSION, FACILITATION AND DEVELOPMENT</div>
    <div class="hero-text">success of a product or service isdetermined always by people whether producers or consumers;<br>fromquality of their working relationships.</div>
  </div>
  <div class="hero-arrow" style="left:56px">
    <svg width="36" height="36" viewBox="0 0 36 36"><polyline points="20,12 14,18 20,24" fill="none" stroke="#fff" stroke-width="2"/></svg>
  </div>
  <div class="hero-arrow" style="left:1106px">
    <svg width="36" height="36" viewBox="0 0 36 36"><polyline points="16,12 22,18 16,24" fill="none" stroke="#fff" stroke-width="2"/></svg>
  </div>
</section>

<section class="what-we-do">
  <h2 class="section-title" style="top:24px">WHAT WE DO</h2>
  <div class="service" style="left:248px">
    <div class="service-icon"><svg width="40" height="36" viewBox="0 0 40 36" fill="none" stroke="#fff" stroke-width="2"><rect x="3" y="3" width="34" height="22"/><line x1="20" y1="25" x2="20" y2="31"/><line x1="12" y1="32" x2="28" y2="32"/><rect x="9" y="9" width="10" height="10"/><line x1="23" y1="10" x2="31" y2="10"/><line x1="23" y1="15" x2="31" y2="15"/></svg></div>
    <div class="service-name">DESIGN</div>
    <div class="service-text">I can show you how to beat<br>the "Big Boxes".The decision<br>how to is yours.</div>
  </div>
  <div class="service" style="left:483px">
    <div class="service-icon"><svg width="36" height="36" viewBox="0 0 36 36" fill="none" stroke="#fff" stroke-width="2"><rect x="5" y="4" width="22" height="28"/><line x1="10" y1="11" x2="22" y2="11"/><line x1="10" y1="17" x2="22" y2="17"/><line x1="10" y1="23" x2="18" y2="23"/><line x1="32" y1="8" x2="20" y2="26"/></svg></div>
    <div class="service-name">FACILITATION</div>
    <div class="service-text">I can show you how to beat<br>the "Big Boxes".The decision<br>how to is yours.</div>
  </div>
  <div class="service" style="left:716px">
    <div class="service-icon"><svg width="40" height="36" viewBox="0 0 40 36" fill="none" stroke="#fff" stroke-width="2"><rect x="3" y="3" width="34" height="24"/><polyline points="8,21 15,14 21,18 31,9"/><line x1="20" y1="27" x2="20" y2="32"/><line x1="12" y1="33" x2="28" y2="33"/></svg></div>
    <div class="service-name">COLLABORATION</div>
    <div class="service-text">I can show you how to beat<br>the "Big Boxes".The decision<br>how to is yours.</div>
  </div>
  <div class="service" style="left:959px">
    <div class="service-icon"><svg width="38" height="38" viewBox="0 0 38 38" fill="none" stroke="#fff" stroke-width="2"><rect x="6" y="3" width="26" height="16"/><circle cx="10" cy="25" r="3"/><circle cx="19" cy="25" r="3"/><circle cx="28" cy="25" r="3"/><line x1="4" y1="35" x2="34" y2="35"/></svg></div>
    <div class="service-name">TRAINING</div>
    <div class="service-text">I can show you how to beat<br>the "Big Boxes".The decision<br>how to is yours.</div>
  </div>
</section>

<section class="mission">
  <div class="mission-visual" role="img" aria-label="Desktop monitor showing the company name on its screen"></div>
  <h2 class="mission-title">OUR MISSION</h2>
  <p class="mission-lead">Our mission is to promote Step flexible organizations</p>
  <p class="mission-text" style="top:1158px">Our mission is to promote Step flexible organizations in which they work in<br>teams, forobjectives, with a less hierarchical.</p>
  <p class="mission-text" style="top:1224px;left:590px">In this framework, DoRuVi fact believes that the success of a product or service<br>isdetermined always by people whether producers or consumers; fromquality of<br>their working relationships.</p>
  <div class="btn-primary">Read More info</div>
</section>

<section class="portfolio">
  <h2 class="section-title" style="top:40px">PORTFOLIO</h2>
  <p class="portfolio-sub">Ability to independently upgradeable as you have the work done</p>
  <div class="work" style="left:132px"><div class="work-img" role="img" aria-label="Photo of a businessman in a dark suit holding an umbrella" style="background:linear-gradient(160deg,#1e3a55,#0d1a27)"></div><div class="work-link">http://www.folio-sample.com</div></div>
  <div class="work" style="left:370px"><div class="work-img" role="img" aria-label="Photo of a businessman touching a digital interface of glowing screens" style="background:linear-gradient(160deg,#0f2c4a,#2c7aa8 55%,#0a1b2d)"></div><div class="work-link">http://www.folio-sample.com</div></div>
  <div class="work" style="left:607px"><div class="work-img" role="img" aria-label="Photo of colleagues gathered around a laptop in an office" style="background:linear-gradient(160deg,#c9cdd2,#8d8790 55%,#4c3f58)"></div><div class="work-link">http://www.folio-sample.com</div></div>
  <div class="work" style="left:845px"><div class="work-img" role="img" aria-label="Photo of hands typing on a silver laptop" style="background:linear-gradient(160deg,#ececec,#d4d4d4 60%,#b9b9b9)"></div><div class="work-link">http://www.folio-sample.com</div></div>
</section>

<section class="blog">
  <h2 class="section-title" style="top:1850px">OUR BLOG</h2>
  <div class="blog-img" role="img" aria-label="Photo of a smiling businesswoman in a blue jacket with her team" style="left:132px;width:205px;background:linear-gradient(160deg,#e7eef5,#9bb8d6 50%,#1f5fb0)"></div>
  <div class="blog-body" style="left:352px">
    <div class="blog-title">Co-Design Stories and Notes<br>written by our team in 2014</div>
    <div class="blog-text">I must explain to you how all this mis-<br>taken idea of denouncing pleasure and<br>praising pain was born and I will give</div>
    <div class="blog-meta"><svg width="12" height="16" viewBox="0 0 12 16"><path d="M6 1a5 5 0 0 0-5 5c0 4 5 9 5 9s5-5 5-9a5 5 0 0 0-5-5z" fill="#333"/><circle cx="6" cy="6" r="2" fill="#fff"/></svg>dignissimos&nbsp;<svg width="15" height="15" viewBox="0 0 15 15"><circle cx="7.5" cy="7.5" r="6.5" fill="#333"/><polyline points="7.5,3.5 7.5,7.5 10,9" fill="none" stroke="#fff" stroke-width="1.5"/></svg>3:00pm to 7:00pm</div>
  </div>
  <div class="blog-img" role="img" aria-label="Photo of a team of colleagues working around a laptop" style="left:607px;width:200px;background:linear-gradient(160deg,#f1f1f1,#c8c2bb 55%,#6e6a74)"></div>
  <div class="blog-body" style="left:831px">
    <div class="blog-title">Co-Design Stories and Notes<br>written by our team in 2014</div>
    <div class="blog-text">I must explain to you how all this mis-<br>taken idea of denouncing pleasure and<br>praising pain was born and I will give</div>
    <div class="blog-meta"><svg width="12" height="16" viewBox="0 0 12 16"><path d="M6 1a5 5 0 0 0-5 5c0 4 5 9 5 9s5-5 5-9a5 5 0 0 0-5-5z" fill="#333"/><circle cx="6" cy="6" r="2" fill="#fff"/></svg>dignissimos&nbsp;<svg width="15" height="15" viewBox="0 0 15 15"><circle cx="7.5" cy="7.5" r="6.5" fill="#333"/><polyline points="7.5,3.5 7.5,7.5 10,9" fill="none" stroke="#fff" stroke-width="1.5"/></svg>3:00pm to 7:00pm</div>
  </div>
</section>

<footer class="site-footer">
  <div class="footer-col" style="left:132px">
    <div class="footer-heading">ABOUT OUR COMPANY</div>
    <div class="footer-brand"><span class="footer-brand-dot"></span><span class="footer-brand-name">DoRuVi</span></div>
    <p class="footer-text" style="margin-top:28px">Other business operations include<br>Joint Venture partnership, Public-<br>Private partnership with Federal<br>and State .Governments, Quarry</p>
  </div>
  <div class="footer-col" style="left:369px">
    <div class="footer-heading">SOCIAL &nbsp; FEED</div>
    <div class="tweet" style="margin-top:18px"><span class="tweet-dot"></span><p class="footer-text">Sed ut perspiciatis unde omnis<br>iste natus error sit voluptatem<br><span class="tweet-date">March 10,2014</span></p></div>
    <div class="tweet"><span class="tweet-dot"></span><p class="footer-text">Sed ut perspiciatis unde omnis<br>iste natus error sit voluptatem<br><span class="tweet-date">March 10,2014</span></p></div>
  </div>
  <div class="footer-col" style="left:608px">
    <div class="footer-heading">CONTACT INFO</div>
    <div style="margin-top:6px">
      <div class="contact-row"><svg width="16" height="14" viewBox="0 0 16 14"><path d="M8 1L1 7h2v6h4V9h2v4h4V7h2z" fill="#8fb6e2"/></svg>Address: 48 Via Lenti, Torino, Italy</div>
      <div class="contact-row"><svg width="14" height="14" viewBox="0 0 14 14"><path d="M3 1l3 3-2 2c1 2 2 3 4 4l2-2 3 3-2 2C6 13 1 8 1 3z" fill="#8fb6e2"/></svg>Phone: (039) 284-1175</div>
      <div class="contact-row"><svg width="16" height="14" viewBox="0 0 16 14"><rect x="1" y="5" width="14" height="8" fill="#8fb6e2"/><rect x="4" y="1" width="8" height="5" fill="none" stroke="#8fb6e2" stroke-width="1.5"/></svg>Fax: (039) 284-1176</div>
      <div class="contact-row"><svg width="16" height="12" viewBox="0 0 16 12"><rect x="1" y="1" width="14" height="10" fill="none" stroke="#8fb6e2" stroke-width="1.5"/><polyline points="1,1 8,7 15,1" fill="none" stroke="#8fb6e2" stroke-width="1.5"/></svg>Email: <b>info@doruvi.it</b></div>
    </div>
  </div>
  <div class="footer-col" style="left:851px">
    <div class="footer-heading">NEWS LETTER</div>
    <p class="footer-text" style="margin-top:10px">Sign up for our newsletter and get<br>the latest news.</p>
    <div class="field">User name</div>
    <div class="field" style="margin-top:13px">Password</div>
    <div class="btn-login">Login</div>
  </div>
  <div class="footer-rule"></div>
  <div class="footer-copy">© DoRuVi 2014 • Privacy Policy</div>
  <div class="footer-social"><span></span><span></span><span></span><span></span><span></span></div>
  <div class="footer-code">C12</div>
</footer>

</body>
</html>
```